Business Card Design Project

We need a buisness card for a new digital sinage company. Our target cliants are small to mediaum buisness who want to advertise on out digital sinage network

Target Market(s)

Small to medium buisness

Industry/Entity Type

Digital

Requirements
Must have
• Must have logo

```html
<!DOCTYPE html>
<html lang="en">
<head>
<meta charset="utf-8">
<title>Vistro Business Card</title>
<link rel="stylesheet" href="https://fonts.googleapis.com/css2?family=Archivo+Black&family=Open+Sans:wght@400;600&display=swap">
<style>
  :root {
    --page: #dcdcdc;
    --ink: #141414;
    --paper: #f4f4f2;
    --green: #4c9a2a;
    --blue: #1f7fc4;
    --orange: #f3a51c;
    --pale-green: #dde8c8;
    --pale-blue: #cfe2ef;
    --pale-orange: #f6dfb2;
    --rule: rgba(20, 20, 20, 0.55);
  }
  * { margin: 0; padding: 0; box-sizing: border-box; }
  html, body {
    width: 1200px; height: 1200px; overflow: hidden;
    background: var(--page);
  }
  .sheet {
    width: 1200px; height: 1200px;
    display: flex; flex-direction: column; align-items: center; justify-content: center;
    gap: 60px;
  }
  .card {
    position: relative;
    width: 900px; height: 514px;
    overflow: hidden;
    background: var(--paper);
    box-shadow: 0 6px 18px rgba(0,0,0,0.18);
  }
  .card-pattern {
    position: absolute; inset: 0;
  }
  .card-back .card-pattern {
    background: linear-gradient(120deg, var(--green) 0%, var(--blue) 35%, var(--orange) 62%, var(--green) 100%);
  }
  .card-front .card-pattern {
    background: linear-gradient(120deg, var(--pale-green) 0%, var(--paper) 30%, var(--pale-orange) 55%, var(--pale-blue) 100%);
  }
  .corner-shape { position: absolute; left: 0; }
  .card-back .corner-shape { top: 0; }
  .card-front .corner-shape { top: 60px; }

  /* back: brand tile */
  .brand-tile {
    position: absolute; left: 70px; top: 60px;
    width: 200px; height: 200px;
    background: var(--paper);
    display: flex; align-items: center; justify-content: center;
  }
  .brand-tile .brand-name {
    font-family: "Archivo Black", sans-serif;
    font-size: 38px; color: var(--ink);
  }

  /* back: contact */
  .contact {
    position: absolute; left: 360px; top: 130px; width: 470px;
    color: var(--ink);
  }
  .contact-name {
    font-family: "Archivo Black", sans-serif;
    font-size: 46px; letter-spacing: 1px;
    text-align: right; margin-bottom: 4px;
  }
  .contact-line {
    font-family: "Open Sans", sans-serif;
    font-size: 20px;
    padding: 6px 0 4px;
    border-bottom: 1.5px solid var(--rule);
    width: 100%;
  }

  /* front: brand */
  .brand-lockup {
    position: absolute; left: 250px; top: 180px;
    display: flex; align-items: center; gap: 34px;
  }
  .brand-square {
    width: 120px; height: 120px;
    background: var(--blue);
  }
  .card-front .brand-name {
    font-family: "Archivo Black", sans-serif;
    font-size: 140px; line-height: 1; color: var(--ink);
  }
</style>
</head>
<body>
<main class="sheet">
  <section class="card card-back">
    <div class="card-pattern" role="img" aria-label="Geometric pattern of green, blue and orange triangles"></div>
    <svg class="corner-shape" width="140" height="240" viewBox="0 0 140 240" aria-hidden="true">
      <polygon points="0,0 140,0 0,240" fill="var(--ink)"/>
    </svg>
    <div class="brand-tile"><span class="brand-name">Vistro</span></div>
    <div class="contact">
      <h1 class="contact-name">SAM LOWE</h1>
      <p class="contact-line">555 010 234</p>
      <p class="contact-line">Adress</p>
      <p class="contact-line">info@vistro.com</p>
      <p class="contact-line">www.vistro.com</p>
    </div>
  </section>

  <section class="card card-front">
    <div class="card-pattern" role="img" aria-label="Faint pastel pattern of green, blue and orange triangles"></div>
    <svg class="corner-shape" width="120" height="200" viewBox="0 0 120 200" aria-hidden="true">
      <polygon points="0,0 120,0 0,200" fill="#333"/>
    </svg>
    <div class="brand-lockup">
      <span class="brand-square" aria-hidden="true"></span>
      <span class="brand-name">Vistro</span>
    </div>
  </section>
</main>
</body>
</html>
```